Lumaform website scandinavian interior design

Existing website: http://lumaform-example.no/

Webdesign for interior designer Ragna Tvedtholm. The company name is Lumaform. Scandinavian interiør is known to be simple and elegant. The website will be in Norwegian, we are working on the text. The website needs to have a few more pages than just the front page. Here are the different titles of the pages:

1. Hjem
2. Om Lumaform
3. Tjenester og priser
4.. Kontakt oss

There should be Facebook and Instagram icons somewhere at the bottom of the website.

The logo we want to use is attached (pink with black print, see attachment )

We have attached images for inspiration. We want to use some of these colors. The color in the logo, The style should be elegant, modern and delicate.

It is imprtant that the website is user friendly.

Target Market(s)

People who want to decorate their home
Companies and public sector who need to redecorate

Industry/Entity Type

Interior Designer

Coding

Coded - Design and coding required

Number of Pages Required

5+ page

Font styles to use
Other font styles liked:
• see example in the logo breakdown

Requirements
Must have
• Elegant, modern and delicate design
Images of design, see examples attached
Colors similar to the pictures
Should not have
• Too bright colors
Pictures of people

```html
<!DOCTYPE html>
<html lang="no">
<head>
<meta charset="utf-8">
<title>Lumaform – Interiørdesign</title>
<link href="https://fonts.googleapis.com/css2?family=Pinyon+Script&family=Lato:wght@400;700&display=swap" rel="stylesheet">
<style>
:root{
  --sage:#98ada7;
  --sage-dark:#7f9891;
  --sage-deep:#667c76;
  --rose:#bf9e91;
  --ink:#222;
  --text:#666;
  --white:#fff;
  --script:"Pinyon Script", cursive;
  --sans:"Lato", sans-serif;
}
*{margin:0;padding:0;box-sizing:border-box}
html,body{width:1200px;height:3705px;overflow:hidden}
body{position:relative;background:var(--white);font-family:var(--sans);color:var(--text)}
.abs{position:absolute}
.photo{position:absolute}
.script{font-family:var(--script);font-weight:400;color:var(--ink)}
.eyebrow{font-size:11px;letter-spacing:.5px;text-transform:uppercase;color:#3d4f4a}
.copy{font-size:11px;line-height:21px;color:var(--text)}
.btn{position:absolute;display:flex;align-items:center;justify-content:center;background:var(--rose);color:var(--white)}
.btn-script{font-family:var(--script);font-size:20px}

/* hero */
.hero{position:absolute;left:0;top:0;width:945px;height:712px;background:var(--sage);border-bottom-right-radius:72px}
.brand{position:absolute;font-family:var(--script);color:var(--white);font-size:40px;line-height:1}
.nav{position:absolute;top:40px;left:502px;font-size:12px;color:var(--white)}
.nav span{position:absolute;white-space:nowrap}
.hero-rule{position:absolute;left:162px;top:104px;width:783px;height:1px;background:rgba(255,255,255,.5)}
.hero-title{position:absolute;left:158px;top:228px;font-family:var(--script);font-weight:400;color:var(--white);font-size:52px;line-height:58px}
.hero-copy{position:absolute;left:162px;top:372px;width:420px;font-size:13px;line-height:22px;color:var(--white)}
.hero-btn{left:162px;top:460px;width:164px;height:50px;background:var(--white);color:var(--ink)}

/* testimonials */
.card{position:absolute;top:2827px;width:278px;height:153px;background:var(--white);box-shadow:0 0 12px rgba(0,0,0,.08)}
.avatar{position:absolute;width:75px;height:88px;border:3px solid #9fb1ac}
.client{position:absolute;font-size:11px;font-weight:700;color:var(--ink)}
.stars{position:absolute;font-size:13px;color:#f07f1c;letter-spacing:3px}
.card-copy{position:absolute;left:16px;top:60px;width:250px;font-size:11px;line-height:19px;color:var(--text)}

/* footer */
.footer{position:absolute;left:0;top:3375px;width:1200px;height:290px;background:linear-gradient(90deg,#7e9891,#96aca5);border-top-right-radius:72px}
.foot-links{position:absolute;top:3500px;left:0;width:1200px;text-align:center;font-size:12px;color:var(--white)}
.foot-links span{margin:0 14px}
.foot-rule{position:absolute;left:162px;top:3548px;width:876px;height:1px;background:rgba(255,255,255,.35)}
.ico{position:absolute;top:3587px;width:38px;height:38px;border:1px solid var(--white);display:flex;align-items:center;justify-content:center}
.foot-text{position:absolute;font-size:11px;line-height:18px;color:var(--white)}
.social{position:absolute;top:3587px;width:38px;height:38px;border:1px solid var(--white)}
.bottom-bar{position:absolute;left:0;top:3665px;width:1200px;height:40px;background:var(--sage-deep);color:var(--white);font-size:11px;text-align:center;line-height:40px}
</style>
</head>
<body>

<!-- HERO -->
<section class="hero"></section>
<div class="brand" style="left:162px;top:28px">Lumaform</div>
<nav class="nav">
  <span style="left:0">HJEM</span>
  <span style="left:58px">OM OSS</span>
  <span style="left:129px">TJENESTER</span>
  <span style="left:217px">KONTAKT OSS</span>
</nav>
<svg class="abs" style="left:846px;top:36px" width="26" height="26" viewBox="0 0 26 26" aria-label="Søk"><circle cx="10" cy="10" r="8" fill="none" stroke="#fff" stroke-width="2.5"/><line x1="16" y1="16" x2="24" y2="24" stroke="#fff" stroke-width="3"/></svg>
<div class="hero-rule"></div>
<h1 class="hero-title">Fleksibel og skreddersydd<br>Interiørdesign</h1>
<p class="hero-copy">Firma Lumaform AS jobber med utvikling av interiørmiljøer for private, bedrifter og offentlige institusjoner.</p>
<div class="btn btn-script hero-btn">La oss snakke</div>
<div class="photo" role="img" aria-label="Stue med lilla sofa og takbelysning" style="left:836px;top:155px;width:240px;height:240px;background:linear-gradient(160deg,#eef0f2,#b9b3c4 60%,#4a3c5e)"></div>
<div class="photo" role="img" aria-label="Stue med grønn peisvegg og bokhylle" style="left:657px;top:340px;width:270px;height:270px;background:linear-gradient(120deg,#c9a55a,#6f9a5c 55%,#8a7a68)"></div>
<div class="photo" role="img" aria-label="Innendørs basseng" style="left:954px;top:404px;width:224px;height:224px;background:linear-gradient(180deg,#e8e4de,#c9b79c 45%,#2d8fd0)"></div>

<!-- OM OSS -->
<div class="photo" role="img" aria-label="Mørk stue med sofa og kunst" style="left:21px;top:803px;width:240px;height:240px;background:linear-gradient(150deg,#4b3a2e,#8a6c54 50%,#c9b6a2)"></div>
<div class="photo" role="img" aria-label="Soverom med hyller" style="left:274px;top:840px;width:300px;height:300px;background:linear-gradient(180deg,#a9a29a,#d8d2c9 60%,#3a3330)"></div>
<div class="photo" role="img" aria-label="Dekor med gullfigurer mot blå vegg" style="left:97px;top:1058px;width:166px;height:165px;background:linear-gradient(135deg,#3f6d7a,#8a7a52 60%,#d06a3a)"></div>
<div class="abs eyebrow" style="left:612px;top:817px;color:#5e736d">OM OSS</div>
<h2 class="abs script" style="left:612px;top:836px;font-size:36px">Velkommen til Lumaform</h2>
<p class="abs copy" style="left:612px;top:888px;width:390px">Firma Lumaform AS jobber med utvikling av interiørmiljøer for private, bedrifter og offentlige institusjoner. For å finne de optimale løsninger til et prosjekt, enten det er et rom eller fler, kreves det kjennskap og kunnskap i markedet. Ved å bruke profesjonell kompetanse på området, sparer du både tid og penger.<br>Bruk av plantegninger/møbleringsplaner, 3D tegninger, Collager eller «lage en levende collage» – så finner vi de beste løsninger for deg som kunde.<br>Målet er alltid kunden i fokus – få det som du/dere vil ha det.</p>
<div class="btn" style="left:612px;top:1104px;width:122px;height:41px;font-size:15px;font-weight:700">Read More</div>

<!-- TJENESTER -->
<div class="abs eyebrow" style="left:0;top:1252px;width:1200px;text-align:center">TJENESTER</div>
<h2 class="abs script" style="left:0;top:1268px;width:1200px;text-align:center;font-size:38px">What We Provide</h2>

<div class="abs" style="left:516px;top:1364px;width:684px;height:375px;background:var(--sage)"></div>
<div class="photo" role="img" aria-label="Stue med mørk sofa og puter" style="left:559px;top:1404px;width:225px;height:300px;background:linear-gradient(180deg,#9a9ea0,#5c5a58 60%,#3a2f2c)"></div>
<div class="photo" role="img" aria-label="Soverom med hvitt sengetøy" style="left:799px;top:1404px;width:225px;height:300px;background:linear-gradient(180deg,#6b625c,#b8aea3 55%,#1e1c1b)"></div>
<div class="photo" role="img" aria-label="Lamper og tørkede blomster" style="left:1039px;top:1404px;width:161px;height:300px;background:linear-gradient(160deg,#3b3a35,#7f6b45 50%,#c7a35d)"></div>
<h3 class="abs script" style="left:162px;top:1404px;font-size:36px">1. Privat interiør</h3>
<p class="abs copy" style="left:162px;top:1474px;width:310px">Trenger du veiledning i forhold til stiler, farger, tekstiler eller tresorter? Kanskje du har et gammelt hus som du skal restaurere, eller kanskje du skal bytte kjøkken? Lumaform hjelper deg gjerne med å finne løsninger som er tilpasset deg og dine behov!</p>
<div class="btn" style="left:162px;top:1618px;width:32px;height:32px"><svg width="16" height="12" viewBox="0 0 16 12"><path d="M15 6H2M6 1 1 6l5 5" fill="none" stroke="#fff" stroke-width="1.5"/></svg></div>
<div class="btn" style="left:208px;top:1618px;width:32px;height:32px"><svg width="16" height="12" viewBox="0 0 16 12"><path d="M1 6h13M10 1l5 5-5 5" fill="none" stroke="#fff" stroke-width="1.5"/></svg></div>

<div class="photo" role="img" aria-label="Korridor med røde stoler og glassvegg" style="left:131px;top:1852px;width:240px;height:240px;background:linear-gradient(120deg,#3b4a3c,#a9b0a8 45%,#6a6d6b)"></div>
<div class="photo" role="img" aria-label="Trehyller med planter mot rosa vegg" style="left:320px;top:1954px;width:240px;height:240px;background:linear-gradient(160deg,#f1dcd3,#e9c9bb 60%,#b7794d)"></div>
<h3 class="abs script" style="left:612px;top:1886px;font-size:36px">2. Bedrift / Offentlig</h3>
<p class="abs copy" style="left:612px;top:1941px;width:330px">Lumaform hjelper deg med bevisst bruk av materialer i forhold til funksjon, design, forskrifter, pris m.m.<br>Kan være din/deres hjelp i prosjektet til å få oversikt, og "nøste trådene sammen" til det beste for alle. Maybe you are planning to build a cabin, but are unsure how to make the most of the space?</p>
<div class="btn btn-script" style="left:612px;top:2083px;width:134px;height:41px;font-size:17px">Utforsk mer</div>

<div class="abs" style="left:919px;top:2228px;width:195px;height:345px;background:var(--rose)"></div>
<div class="photo" role="img" aria-label="Spisestue med rundt bord og lampe" style="left:769px;top:2243px;width:330px;height:315px;background:linear-gradient(170deg,#e9e9ea,#c7b7a4 55%,#6a5a4c)"></div>
<div class="photo" role="img" aria-label="Stue med sittegruppe og teppe" style="left:612px;top:2300px;width:202px;height:202px;background:linear-gradient(180deg,#cfcac2,#6d6a64 55%,#e7e2da);border:3px solid #fff"></div>
<h3 class="abs script" style="left:162px;top:2290px;font-size:36px">3. leverandører</h3>
<p class="abs copy" style="left:162px;top:2350px;width:320px">Lumaform AS har gjennom flere år, brukt tid på å opparbeide seg gode kontakter i markedet. Dette har gitt resultater! Dyktige og seriøse underleverandører av varer og tjenester av høyeste kvalitet. God dialog og god kommunikasjon er nøkkelen i ethvert prosjekt.</p>
<div class="btn btn-script" style="left:162px;top:2489px;width:135px;height:41px;font-size:17px">Utforsk mer</div>

<!-- TESTIMONIALER -->
<div class="abs" style="left:162px;top:2633px;font-size:15px;color:#3d4f4a">VÅRE TESTIMONIALER</div>
<h2 class="abs script" style="left:162px;top:2662px;font-size:38px">Hva vår klient sier</h2>
<p class="abs copy" style="left:538px;top:2652px;width:430px;line-height:19px">Lorem Ipsum er ganske enkelt dummitekst fra trykkeri- og typebransjen. Lorem Ipsum har vært bransjens standard dummy-tekst.</p>

<div class="card" style="left:162px"><p class="card-copy">Lorem Ipsum er ganske enkelt dummitekst fra trykkeri- og typebransjen. Lorem Ipsum har vært bransjens standard dummy-tekst helt siden 1500-tallet.</p></div>
<div class="card" style="left:462px"><p class="card-copy">Lorem Ipsum er ganske enkelt dummitekst fra trykkeri- og typebransjen. Lorem Ipsum har vært bransjens standard dummy-tekst helt siden 1500-tallet.</p></div>
<div class="card" style="left:762px"><p class="card-copy">Lorem Ipsum er ganske enkelt dummitekst fra trykkeri- og typebransjen. Lorem Ipsum har vært bransjens standard dummy-tekst helt siden 1500-tallet.</p></div>
<div class="avatar" role="img" aria-label="Portrett av klient" style="left:176px;top:2785px;background:linear-gradient(180deg,#8c8f93,#3f6f9a)"></div>
<div class="avatar" role="img" aria-label="Portrett av klient" style="left:476px;top:2785px;background:linear-gradient(180deg,#9aa3ab,#5d7f9f)"></div>
<div class="avatar" role="img" aria-label="Portrett av klient" style="left:776px;top:2785px;background:linear-gradient(180deg,#3a3030,#7a5a4c)"></div>
<div class="client" style="left:267px;top:2846px">Client Name</div>
<div class="client" style="left:567px;top:2846px">Client Name</div>
<div class="client" style="left:867px;top:2846px">Client Name</div>
<div class="stars" style="left:267px;top:2862px">★★★★★</div>
<div class="stars" style="left:567px;top:2862px">★★★★★</div>
<div class="stars" style="left:867px;top:2862px">★★★★★</div>

<!-- NYHETSBREV -->
<div class="abs eyebrow" style="left:0;top:3062px;width:1200px;text-align:center">NYHETSBREV</div>
<h2 class="abs script" style="left:0;top:3080px;width:1200px;text-align:center;font-size:38px">Abonner nå!</h2>
<p class="abs copy" style="left:400px;top:3138px;width:400px;text-align:center">Lorem Ipsum er ganske enkelt dummitekst fra trykkeri- og typebransjen. Lorem Ipsum har vært bransjens standard dummy-tekst.</p>
<div class="abs" style="left:432px;top:3192px;width:336px;height:36px;border:1px solid #e3e3e3;font-size:11px;color:#777;padding:11px 12px">Skriv inn e-post:</div>
<div class="btn btn-script" style="left:532px;top:3255px;width:135px;height:41px;font-size:17px">Skriv inn OTP</div>

<!-- FOOTER -->
<footer class="footer"></footer>
<div class="brand" style="left:0;width:1200px;text-align:center;top:3425px">Lumaform</div>
<div class="foot-links"><span>Hjem</span><span>Om Oss</span><span>Tjenester</span><span>Kontakt Oss</span></div>
<div class="foot-rule"></div>
<div class="ico" style="left:162px"><svg width="18" height="18" viewBox="0 0 24 24"><path d="M6.6 10.8a15 15 0 0 0 6.6 6.6l2.2-2.2c.3-.3.7-.4 1-.2 1.1.4 2.3.6 3.6.6.6 0 1 .4 1 1V20c0 .6-.4 1-1 1A17 17 0 0 1 3 4c0-.6.4-1 1-1h3.5c.6 0 1 .4 1 1 0 1.3.2 2.5.6 3.6.1.3 0 .7-.2 1z" fill="#fff"/></svg></div>
<div class="foot-text" style="left:211px;top:3597px">+4791234560</div>
<div class="ico" style="left:386px"><svg width="18" height="14" viewBox="0 0 18 14"><rect x="1" y="1" width="16" height="12" fill="none" stroke="#fff" stroke-width="1.5"/><path d="M1 1l8 7 8-7" fill="none" stroke="#fff" stroke-width="1.5"/></svg></div>
<div class="foot-text" style="left:436px;top:3597px">post@lumaform-example.no</div>
<div class="ico" style="left:612px"><svg width="14" height="18" viewBox="0 0 14 18"><path d="M7 17S1 10 1 6.5a6 6 0 0 1 12 0C13 10 7 17 7 17z" fill="none" stroke="#fff" stroke-width="1.5"/><circle cx="7" cy="6.5" r="2" fill="#fff"/></svg></div>
<div class="foot-text" style="left:662px;top:3588px">Lumaform As v/ Ragna Tvedtholm,<br>Lyngveien 14, 3050 Solbakk</div>
<div class="social" aria-hidden="true" style="left:852px"></div>
<div class="social" aria-hidden="true" style="left:898px"></div>
<div class="bottom-bar">Copyright © 2020 Lumaform. Alle rettigheter forbeholdt. Vilkår og betingelser | Personvern.</div>

</body>
</html>
```